Newsletter Banner Ad with a URL to our website offering

We need a banner ad for a newsletter that is published to members biweekly that simply articulates our value proposition and enables the reader to click on our logo to learn more and engage with us to schedule an Emergency Response Plan so they are ready for when a burst pipe happens on their property. They will have a plan after they engage with us.
We need quotes to build two options 1&2

```html
<!DOCTYPE html>
<html lang="en">
<head>
<meta charset="utf-8">
<title>Tidewell Restoration – Rapid Response Plan Banner</title>
<link rel="stylesheet" href="https://fonts.googleapis.com/css2?family=Montserrat:wght@700&display=swap">
<style>
  :root {
    --brand-blue: #2c3a8f;
    --brand-red: #d3262d;
    --ring-grey: #dcdde0;
    --spray-light: #f1f3f4;
    --spray-mid: #cfd4d8;
    --spray-dark: #a3acb2;
    --white: #ffffff;
  }
  * { box-sizing: border-box; margin: 0; padding: 0; }
  html, body {
    width: 1200px;
    height: 310px;
    overflow: hidden;
    background: var(--white);
  }
  .banner {
    position: relative;
    width: 1200px;
    height: 310px;
    overflow: hidden;
    font-family: "Montserrat", Arial, sans-serif;
  }
  .banner-shapes {
    position: absolute;
    inset: 0;
  }
  .brand-badge {
    position: absolute;
    left: 67px;
    top: 78px;
    width: 180px;
    height: 180px;
    border-radius: 50%;
    display: flex;
    align-items: center;
    justify-content: center;
    text-decoration: none;
  }
  .brand-name {
    color: var(--brand-blue);
    font-weight: 700;
    font-size: 25px;
    line-height: 1.2;
    text-align: center;
    width: 150px;
  }
  .headline {
    position: absolute;
    right: 30px;
    top: 124px;
    color: var(--white);
    font-weight: 700;
    font-size: 34px;
    line-height: 1.3;
    letter-spacing: 0.3px;
    text-align: right;
    text-transform: uppercase;
  }
  .headline span { display: block; }
</style>
</head>
<body>
  <div class="banner">
    <svg class="banner-shapes" width="1200" height="310" viewBox="0 0 1200 310">
      <defs>
        <linearGradient id="spray-fill" x1="0" y1="0" x2="1" y2="1">
          <stop offset="0" stop-color="var(--spray-light)"/>
          <stop offset="0.55" stop-color="var(--spray-mid)"/>
          <stop offset="1" stop-color="var(--spray-dark)"/>
        </linearGradient>
      </defs>

      <rect class="brand-field" x="0" y="0" width="240" height="310" fill="var(--brand-blue)"/>

      <rect class="sprinkler-photo" x="200" y="0" width="500" height="310" fill="url(#spray-fill)"
            role="img" aria-label="Photo of a red fire sprinkler head spraying water"/>

      <path class="message-panel" d="M680 0 H1200 V310 H590 C630 210 655 100 680 0 Z" fill="var(--brand-blue)"/>

      <circle class="ring-outer" cx="157" cy="168" r="178" fill="var(--ring-grey)"/>
      <circle class="ring-blue" cx="157" cy="168" r="160" fill="var(--brand-blue)"/>
      <circle class="ring-red" cx="157" cy="168" r="136" fill="var(--brand-red)"/>
      <circle class="badge-face" cx="157" cy="168" r="96" fill="var(--white)"/>
    </svg>

    <a class="brand-badge" href="#" aria-label="Tidewell Restoration – learn more">
      <span class="brand-name">Tidewell Restoration</span>
    </a>

    <h1 class="headline">
      <span>Do you have a rapid</span>
      <span>response plan for this?</span>
    </h1>
  </div>
</body>
</html>
```